Creative Design "Size Chart" for a Clothing Product

Hi, My dear friends! I am looking to do a contest to design a unique creative "Size Chart" for our clothing line. See Attached the Sizes & Ideas Thanks Good Luck Dolph

Colors

Designer to choose colors to be used in the design.

```html
<!DOCTYPE html>
<html lang="en">
<head>
<meta charset="utf-8">
<title>Size Chart</title>
<link rel="stylesheet" href="https://fonts.googleapis.com/css2?family=Pacifico&family=Roboto:wght@400;700&display=swap">
<style>
  :root{
    --purple-bg:#4a2878;
    --purple-head:#2c1a4e;
    --purple-row-a:#4f2d83;
    --purple-row-b:#452674;
    --red-bg:#c83a4d;
    --red-head:#982536;
    --red-row-a:#c4485a;
    --red-row-b:#b93d4f;
    --white:#ffffff;
    --stitch:rgba(255,255,255,.45);
    --tee:#1b1b1d;
    --polo:#f1f1f1;
    --tee-label:#d9d9d9;
    --polo-label:#c8323f;
  }
  *{margin:0;padding:0;box-sizing:border-box}
  html,body{width:1200px;height:1200px;overflow:hidden;background:var(--purple-bg)}
  .canvas{width:1000px;height:1000px;transform:scale(1.2);transform-origin:0 0;position:relative;font-family:'Roboto',Arial,sans-serif;color:var(--white)}
  .panel{position:absolute;left:0;width:1000px;height:500px}
  .panel--men{top:0;background:radial-gradient(ellipse at center,#55308a 0%,var(--purple-bg) 70%)}
  .panel--women{top:500px;background:radial-gradient(ellipse at center,#d4465a 0%,var(--red-bg) 70%)}
  .stitch{position:absolute;left:15px;top:15px;right:15px;bottom:15px;border:2px dashed var(--stitch)}
  .title{position:absolute;font-family:'Pacifico',cursive;font-size:34px;line-height:1;transform:translateX(-50%);text-shadow:0 2px 3px rgba(0,0,0,.25);white-space:nowrap}
  .chart{position:absolute;border-collapse:collapse;text-align:center;box-shadow:0 8px 18px rgba(0,0,0,.3)}
  .chart th{font-weight:700}
  .chart--purple th{background:var(--purple-head)}
  .chart--purple tr:nth-child(odd) td{background:var(--purple-row-a)}
  .chart--purple tr:nth-child(even) td{background:var(--purple-row-b)}
  .chart--red th{background:var(--red-head)}
  .chart--red tr:nth-child(odd) td{background:var(--red-row-a)}
  .chart--red tr:nth-child(even) td{background:var(--red-row-b)}
  .chart--large{width:273px}
  .chart--large th{height:50px;font-size:15px}
  .chart--large td{height:50px;font-size:17px}
  .chart--small{width:234px}
  .chart--small th{height:41px;font-size:12.5px}
  .chart--small td{height:43px;font-size:14.5px}
  .chart--small td:first-child{font-size:12.5px}
  .garment{position:absolute}
  .garment__label{position:absolute;left:0;right:0;text-align:center;font-weight:700;font-size:17px}
</style>
</head>
<body>
<div class="canvas">

  <section class="panel panel--men">
    <div class="stitch"></div>
    <h2 class="title" style="left:176px;top:38px">Mens</h2>
    <table class="chart chart--purple chart--large" style="left:40px;top:100px">
      <tr><th>Size</th><th>Chest</th><th>Waist</th></tr>
      <tr><td>S</td><td>34-36</td><td>28-30</td></tr>
      <tr><td>M</td><td>36-38</td><td>30-32</td></tr>
      <tr><td>L</td><td>38-40</td><td>32-34</td></tr>
      <tr><td>XL</td><td>40-42</td><td>34-36</td></tr>
      <tr><td>2X</td><td>43-45</td><td>36-40</td></tr>
      <tr><td>3X</td><td>45-48</td><td>40-44</td></tr>
    </table>

    <div class="garment" style="left:352px;top:62px;width:286px;height:378px">
      <svg width="286" height="378" role="img" aria-label="Black t-shirt on a wooden hanger with chest and waist measuring lines">
        <rect x="0" y="0" width="286" height="378" rx="14" fill="var(--tee)"/>
        <ellipse cx="143" cy="164" rx="80" ry="8" fill="none" stroke="var(--tee-label)" stroke-width="2" stroke-dasharray="6 4"/>
        <ellipse cx="143" cy="314" rx="80" ry="8" fill="none" stroke="var(--tee-label)" stroke-width="2" stroke-dasharray="6 4"/>
      </svg>
      <span class="garment__label" style="top:177px;color:var(--tee-label)">CHEST</span>
      <span class="garment__label" style="top:328px;color:var(--tee-label)">WAIST</span>
    </div>

    <h2 class="title" style="left:823px;top:38px">Boys</h2>
    <table class="chart chart--purple chart--large" style="left:687px;top:100px">
      <tr><th>Size</th><th>Chest</th><th>Waist</th></tr>
      <tr><td>XXS</td><td>20-23</td><td>19-21</td></tr>
      <tr><td>XS</td><td>23-26</td><td>21-23</td></tr>
      <tr><td>S</td><td>26-29</td><td>32-25</td></tr>
      <tr><td>M</td><td>29-32</td><td>25-27</td></tr>
      <tr><td>L</td><td>32-35</td><td>27-29</td></tr>
      <tr><td>XL</td><td>35-38</td><td>29-31</td></tr>
    </table>
  </section>

  <section class="panel panel--women">
    <div class="stitch"></div>
    <h2 class="title" style="left:177px;top:38px">Womens</h2>
    <table class="chart chart--red chart--small" style="left:60px;top:97px">
      <tr><th>Size</th><th>Chest</th><th>Waist</th></tr>
      <tr><td>XS (0-2)</td><td>32-34</td><td>26-28</td></tr>
      <tr><td>S (4-6)</td><td>34-36</td><td>28-30</td></tr>
      <tr><td>M (8-10)</td><td>36-38</td><td>30-32</td></tr>
      <tr><td>L (12-14)</td><td>38-40</td><td>32-34</td></tr>
      <tr><td>XL (14-16 )</td><td>40-42</td><td>34-36</td></tr>
      <tr><td>2X (18)</td><td>42-44</td><td>36-38</td></tr>
      <tr><td>3X (20)</td><td>44-46</td><td>38-40</td></tr>
    </table>

    <div class="garment" style="left:345px;top:110px;width:290px;height:328px">
      <svg width="290" height="328" role="img" aria-label="White fitted polo shirt with chest and waist measuring lines">
        <rect x="0" y="0" width="290" height="328" rx="14" fill="var(--polo)"/>
        <ellipse cx="145" cy="134" rx="86" ry="8" fill="none" stroke="var(--polo-label)" stroke-width="2" stroke-dasharray="6 4"/>
        <ellipse cx="145" cy="246" rx="78" ry="8" fill="none" stroke="var(--polo-label)" stroke-width="2" stroke-dasharray="6 4"/>
      </svg>
      <span class="garment__label" style="top:154px;color:var(--polo-label)">CHEST</span>
      <span class="garment__label" style="top:262px;color:var(--polo-label)">WAIST</span>
    </div>

    <h2 class="title" style="left:822px;top:38px">Girls</h2>
    <table class="chart chart--red chart--small" style="left:706px;top:97px">
      <tr><th>Size</th><th>Chest</th><th>Waist</th></tr>
      <tr><td>XXS</td><td>19-22</td><td>18-20</td></tr>
      <tr><td>XS</td><td>22-25</td><td>20-22</td></tr>
      <tr><td>S</td><td>25-28</td><td>22-24</td></tr>
      <tr><td>M</td><td>28-31</td><td>24-26</td></tr>
      <tr><td>L</td><td>31-34</td><td>26-28</td></tr>
      <tr><td>XL</td><td>34-37</td><td>28-30</td></tr>
    </table>
  </section>

</div>
</body>
</html>
```